Home page design for a live auction website.

Hi, we are looking at finding a good design for an auction website, only home page .. We will not be selling anything online, so the website will only be a portal where visitors can check about our company, upcoming auctions, online catalogues etc.
See attached our logo. Please use the same red that you see on the logo in the designs that you provide.
The final design should communicate high-end auction website, as we will be selling expensive piece of arts and antiques.
We should have a main frame where images of arts will circulate, with description of the art piece. just like on http://paris.vellmarotte-quisande.com/
(but with a better design overall) and of course a menu with different tabs, like "about us", "previous sales" "next sales", "contact" , "how to buy", "meet our specialists".

Target Market(s)

High end segment, who can afford to pay up to 250'000 for a piece of art

Industry/Entity Type

Online

Number of Pages Required

1 page

Requirements
Must have
• a frame with images rotating, just like on http://paris.vellmarotte-quisande.com/ . but the rest of the design should be more refined.
• we should also have a strong call to action, "Free online estimation", click here, estimation delivered in 48 hours"
Nice to have
• Tremaux Auctions, the brand should be well visible

```html
<!DOCTYPE html>
<html lang="en">
<head>
<meta charset="utf-8">
<title>Tremaux Auctions – Home</title>
<link rel="stylesheet" href="https://fonts.googleapis.com/css2?family=Open+Sans:wght@400;600;700&display=swap">
<style>
:root{
  --red:#c0282d;
  --red-dark:#9e1f23;
  --ink:#333333;
  --muted:#777777;
  --line:#e2e2e2;
  --paper:#ffffff;
  --page:#f4f4f4;
  --footer:#2b2b2b;
  --footer-text:#bdbdbd;
}
*{margin:0;padding:0;box-sizing:border-box}
html,body{width:773px;height:1200px;overflow:hidden}
body{font-family:"Open Sans",Arial,sans-serif;color:var(--ink);background:var(--paper);font-size:9px;line-height:1.45}
.container{width:646px;margin:0 auto;position:relative}

/* header */
.site-header{height:68px}
.site-header .container{display:flex;align-items:center;height:68px}
.brand{display:flex;align-items:center;gap:7px;color:var(--red);font-weight:700;font-size:15px;letter-spacing:.5px}
.brand-dot{width:22px;height:22px;border-radius:50%;background:var(--red)}
.social{display:flex;gap:6px;margin-left:60px}
.social span{width:15px;height:15px;border-radius:3px;background:#9a9a9a}
.lang{margin-left:50px;width:72px;height:20px;border:1px solid var(--line);font-size:8px;color:var(--muted);display:flex;align-items:center;justify-content:space-between;padding:0 6px}
.search{margin-left:auto;display:flex}
.search-field{width:130px;height:22px;border:1px solid var(--line);font-size:8px;color:#aaa;padding:0 7px;display:flex;align-items:center}
.search-btn{width:25px;height:22px;background:var(--red);display:flex;align-items:center;justify-content:center}

/* nav */
.main-nav{background:var(--red);height:22px}
.main-nav ul{list-style:none;display:flex;justify-content:center;gap:26px;height:22px;align-items:center}
.main-nav li{color:#fff;font-size:7.5px;font-weight:600;letter-spacing:.3px}
.main-nav li.caret::after{content:" ▾";font-size:6px}

/* hero */
.hero{position:relative;height:375px;background:linear-gradient(160deg,#6b5a44 0%,#8a7a5e 30%,#4f4a3c 60%,#2f2c24 100%)}
.hero-badge{position:absolute;left:360px;top:40px;width:210px;height:210px;border-radius:50%;background:var(--paper);border:6px solid rgba(255,255,255,.6);background-clip:padding-box;display:flex;flex-direction:column;align-items:center;justify-content:center;text-align:center}
.hero-badge .brand-dot{width:34px;height:34px;margin-bottom:8px}
.hero-name{color:var(--red);font-weight:700;font-size:16px;letter-spacing:.6px}
.hero-tag{font-size:8px;font-weight:600;color:var(--ink);letter-spacing:1px;margin:3px 0 12px}
.btn{display:inline-block;background:var(--red);color:#fff;font-weight:600;font-size:7.5px;letter-spacing:.4px;padding:5px 12px}
.hero-strip{position:absolute;left:63.5px;top:195px;width:646px;height:128px;background:var(--paper);border-top:3px solid var(--red);display:flex;gap:10px;padding:10px;box-shadow:0 2px 6px rgba(0,0,0,.25)}
.strip-item{flex:1;display:flex;flex-direction:column}
.strip-photo{height:80px}
.strip-caption{display:flex;align-items:center;gap:5px;margin-top:9px;font-size:7px;font-weight:600}
.arrow-sq{width:12px;height:12px;background:var(--red);display:flex;align-items:center;justify-content:center}
.tone-a{background:linear-gradient(135deg,#cfc6a8,#8c7c55)}
.tone-b{background:linear-gradient(135deg,#6f7d86,#3e4a52)}
.tone-c{background:linear-gradient(135deg,#b89a6c,#6e5233)}
.tone-d{background:linear-gradient(135deg,#a48f74,#4d3c2c)}

/* about */
.about{margin-top:40px;display:flex;gap:22px}
.about-text{flex:1}
.section-title{font-size:12px;font-weight:700;color:var(--ink);letter-spacing:.3px}
.about-text p{color:var(--muted);margin:8px 0 10px;font-size:8px}
.about-photo{width:130px;height:110px;background:linear-gradient(135deg,#3a2f28,#8a6a45 60%,#d6c39a)}

/* previous sales */
.sales-head{margin-top:30px;display:flex;align-items:center;gap:10px}
.sales-head .rule{flex:1;height:1px;background:var(--line)}
.pager{display:flex;gap:3px}
.pager span{width:14px;height:14px;border:1px solid var(--line);display:flex;align-items:center;justify-content:center}
.cards{display:flex;gap:14px;margin-top:18px}
.card{flex:1;border:1px solid var(--line);padding:5px;height:272px;display:flex;flex-direction:column}
.card-photo{height:118px}
.card-title{color:var(--red);font-weight:700;font-size:8px;margin-top:10px}
.card p{color:var(--muted);font-size:7.5px;margin-top:4px}
.card-foot{margin-top:auto;display:flex;align-items:center;justify-content:space-between;padding:0 3px 6px}
.card-foot .btn{font-size:7px;padding:4px 8px}
.price{font-weight:700;font-size:13px;color:var(--ink)}

/* news */
.news-head{margin-top:24px}
.news{display:flex;gap:40px;margin-top:14px}
.news-item{flex:1;display:flex;gap:10px}
.date{width:44px;height:48px;border:1px solid var(--line);text-align:center;flex-shrink:0}
.date .month{background:var(--red);color:#fff;font-weight:700;font-size:8px;padding:3px 0}
.date .day{font-weight:700;font-size:9px;padding-top:8px}
.news-item h3{font-size:7.5px;color:var(--red);font-weight:700}
.news-item p{color:var(--muted);font-size:7.5px;margin-top:2px}

/* footer */
.site-footer{position:absolute;left:0;top:1126px;width:773px;height:74px;background:var(--footer);text-align:center;padding-top:20px}
.site-footer ul{list-style:none;display:flex;justify-content:center;gap:24px}
.site-footer li{color:#fff;font-size:7px;font-weight:600}
.site-footer .copy{color:var(--footer-text);font-size:7px;margin-top:10px}
</style>
</head>
<body>

<header class="site-header">
  <div class="container">
    <div class="brand"><span class="brand-dot"></span>TREMAUX AUCTIONS</div>
    <div class="social"><span></span><span></span><span></span><span></span></div>
    <div class="lang">ENGLISH <span>▾</span></div>
    <div class="search">
      <div class="search-field">search here...</div>
      <div class="search-btn">
        <svg width="10" height="10" viewBox="0 0 10 10"><circle cx="4" cy="4" r="3" fill="none" stroke="#fff" stroke-width="1.4"/><line x1="6.2" y1="6.2" x2="9.2" y2="9.2" stroke="#fff" stroke-width="1.4"/></svg>
      </div>
    </div>
  </div>
</header>

<nav class="main-nav">
  <ul>
    <li>HOME</li><li>ABOUT US</li><li class="caret">PREVIOUS SALES</li><li class="caret">NEXT SALES</li><li>CONTACT</li><li class="caret">HOW TO BUY</li><li>MEET OUR SPECIALISTS</li>
  </ul>
</nav>

<section class="hero" role="img" aria-label="Photograph of an old European canal street with stone buildings and a bridge">
  <div class="hero-badge">
    <span class="brand-dot"></span>
    <div class="hero-name">TREMAUX AUCTIONS</div>
    <div class="hero-tag">THE ARTS AND ANTIQUES</div>
    <span class="btn">GET STARTED</span>
  </div>
  <div class="hero-strip">
    <div class="strip-item"><div class="strip-photo tone-a" role="img" aria-label="Antique pocket watch"></div><div class="strip-caption"><span class="arrow-sq"><svg width="6" height="6" viewBox="0 0 6 6"><path d="M2 1l2 2-2 2" fill="none" stroke="#fff" stroke-width="1.2"/></svg></span>FACER RECTIQUE NEC</div></div>
    <div class="strip-item"><div class="strip-photo tone-b" role="img" aria-label="Vintage mechanical clock parts"></div><div class="strip-caption"><span class="arrow-sq"><svg width="6" height="6" viewBox="0 0 6 6"><path d="M2 1l2 2-2 2" fill="none" stroke="#fff" stroke-width="1.2"/></svg></span>FACER RECTIQUE NEC</div></div>
    <div class="strip-item"><div class="strip-photo tone-c" role="img" aria-label="Collection of antique objects"></div><div class="strip-caption"><span class="arrow-sq"><svg width="6" height="6" viewBox="0 0 6 6"><path d="M2 1l2 2-2 2" fill="none" stroke="#fff" stroke-width="1.2"/></svg></span>FACER RECTIQUE NEC</div></div>
    <div class="strip-item"><div class="strip-photo tone-d" role="img" aria-label="Antique camera on a table"></div><div class="strip-caption"><span class="arrow-sq"><svg width="6" height="6" viewBox="0 0 6 6"><path d="M2 1l2 2-2 2" fill="none" stroke="#fff" stroke-width="1.2"/></svg></span>FACER RECTIQUE NEC</div></div>
  </div>
</section>

<main class="container">
  <section class="about">
    <div class="about-text">
      <h2 class="section-title">ABOUT TREMAUX AUCTIONS</h2>
      <p>Mi ugam imperdiet in vestibulum consequat ac nisi. Duis tempor blandit dui, ac varius sem dapibus et. Fusce aliquam cursus nibh, ac finibus eros gravida quis. Nullam porta magna id mauris volutpat, eget pretium augue tincidunt. Vivamus sed tellus vitae lorem faucibus tristique nec sed ligula. Integer posuere, nisl at laoreet tempus, turpis risus luctus sapien, in congue lectus arcu vel nunc.</p>
      <span class="btn">READ MORE</span>
    </div>
    <div class="about-photo" role="img" aria-label="Antique pocket watch on a chain"></div>
  </section>

  <div class="sales-head">
    <h2 class="section-title">PREVIOUS SALES</h2>
    <span class="rule"></span>
    <div class="pager">
      <span><svg width="6" height="6" viewBox="0 0 6 6"><path d="M4 1L2 3l2 2" fill="none" stroke="#888" stroke-width="1.2"/></svg></span>
      <span><svg width="6" height="6" viewBox="0 0 6 6"><path d="M2 1l2 2-2 2" fill="none" stroke="#888" stroke-width="1.2"/></svg></span>
    </div>
  </div>

  <section class="cards">
    <article class="card"><div class="card-photo tone-c" role="img" aria-label="Shelf of antique porcelain and objects"></div><h3 class="card-title">NAM VIRIS STRO EXPLICARI</h3><p>Mi ugam imperdiet in vestibulum consequat ac nisi tempor</p><div class="card-foot"><span class="btn">VIEW DETAILS</span><span class="price">$ 454.00</span></div></article>
    <article class="card"><div class="card-photo tone-d" role="img" aria-label="Antique shop interior"></div><h3 class="card-title">NAM VIRIS STRO EXPLICARI</h3><p>Mi ugam imperdiet in vestibulum consequat ac nisi tempor</p><div class="card-foot"><span class="btn">VIEW DETAILS</span><span class="price">$ 454.00</span></div></article>
    <article class="card"><div class="card-photo tone-c" role="img" aria-label="Carved wooden cabinet with glass doors"></div><h3 class="card-title">NAM VIRIS STRO EXPLICARI</h3><p>Mi ugam imperdiet in vestibulum consequat ac nisi tempor</p><div class="card-foot"><span class="btn">VIEW DETAILS</span><span class="price">$ 454.00</span></div></article>
    <article class="card"><div class="card-photo tone-a" role="img" aria-label="Vintage automobile"></div><h3 class="card-title">NAM VIRIS STRO EXPLICARI</h3><p>Mi ugam imperdiet in vestibulum consequat ac nisi tempor</p><div class="card-foot"><span class="btn">VIEW DETAILS</span><span class="price">$ 454.00</span></div></article>
  </section>

  <h2 class="section-title news-head">NEWS EVENTS</h2>
  <section class="news">
    <div class="news-item"><div class="date"><div class="month">SEPT</div><div class="day">24 , 2015</div></div><div><h3>DUIS PERPETUS ULLAMCORPER AT</h3><p>Mi ugam imperdiet in vestibulum consequat ac nisi. Duis tempor blandit dui.</p></div></div>
    <div class="news-item"><div class="date"><div class="month">SEPT</div><div class="day">24 , 2015</div></div><div><h3>DUIS PERPETUS ULLAMCORPER AT</h3><p>Mi ugam imperdiet in vestibulum consequat ac nisi. Duis tempor blandit dui.</p></div></div>
  </section>
</main>

<footer class="site-footer">
  <ul><li>HOME</li><li>ABOUT US</li><li>PREVIOUS SALES</li><li>NEXT SALES</li><li>CONTACT</li><li>HOW TO BUY</li><li>MEET OUR SPECIALISTS</li></ul>
  <div class="copy">info@tremauxauctions.com | copyright 2015 tremauxauctions.com</div>
</footer>

</body>
</html>
```